KORPIX POSTCARD

I submitted my postcard and printer said it is not acceptable here are the comments
Item 948762 - Front file: Uploaded png is 3.3 x 2.2" at 300 dpi. Back file: Uploaded png is 5 x 3.3" at 200 dpi. There is text and images too close to the edges for the front and back. Both front/back files are low resolution and have poor print quality. The correct size for a jumbo postcard is 8.75 x 5.75". The intended bleed extends to the edges and all important text and/or elements are to remain at least 3/8" away from the edges. Try saving as a PDF from the source file at the correct size for a possible better printing output.

Item 948763 - Front file: Uploaded jpg is 7 x 5" at 200 dpi. Back file: Uploaded jpg is 8 x 5" at 220 dpi. Both front/back files are low resolution and have poor print quality. The correct size for a Medium TLRS card is 8.25 x 6.75" The intended bleed extends to the edges of the canvas and all important text and/or elements are to remain at least 3/8" away from the edges. Try saving as a PDF from the source file at the correct size for a possible better printing output.

```html
<!DOCTYPE html>
<html lang="en">
<head>
<meta charset="utf-8">
<title>Marisol Venhart, MD – Primary Care</title>
<link rel="stylesheet" href="https://fonts.googleapis.com/css2?family=Montserrat:wght@700;800&family=Lato:wght@300;400;700&display=swap">
<style>
  :root {
    --red: #c32024;
    --yellow: #f3d626;
    --blue: #2279bd;
    --blue-deep: #236b9f;
    --ink: #333333;
    --mist: #f3f3f3;
    --white: #ffffff;
    --photo-a: #e9c6b4;
    --photo-b: #6fb3c9;
  }
  * { margin: 0; padding: 0; box-sizing: border-box; }
  html, body { width: 1200px; height: 982px; overflow: hidden; background: var(--white); }
  .card { position: relative; width: 1200px; height: 982px; overflow: hidden; background: var(--white); }
  .backdrop { position: absolute; inset: 0; width: 1200px; height: 982px; }
  .portrait {
    position: absolute; left: 46px; top: 120px; width: 235px; height: 235px; border-radius: 50%;
    background: radial-gradient(circle at 50% 35%, var(--photo-a) 0 38%, var(--photo-b) 75%);
  }
  .languages { position: absolute; left: 304px; top: 51px; font-family: 'Lato', sans-serif; font-size: 27px; line-height: 27px; }
  .languages .spanish { color: var(--red); font-weight: 400; }
  .languages .tele { color: var(--ink); font-weight: 700; }
  .doctor-name {
    position: absolute; left: 304px; top: 214px; width: 270px; color: var(--white);
    font-family: 'Montserrat', sans-serif; font-weight: 800; font-size: 35px; line-height: 43px; letter-spacing: 0.3px;
  }
  .headline { position: absolute; left: 54px; top: 0; width: 531px; height: 520px; text-align: center; }
  .headline .cares {
    position: absolute; top: 402px; width: 100%; color: var(--blue);
    font-family: 'Montserrat', sans-serif; font-weight: 800; font-size: 38px; line-height: 46px;
  }
  .headline .trust {
    position: absolute; top: 454px; width: 100%; color: var(--red);
    font-family: 'Lato', sans-serif; font-weight: 300; font-size: 38.5px; line-height: 46px; white-space: nowrap;
  }
  .bio {
    position: absolute; left: 55px; top: 560px; width: 531px; color: var(--white);
    font-family: 'Lato', sans-serif; font-size: 20.3px; line-height: 32px; letter-spacing: -0.3px; text-align: justify;
  }
  .bio p + p { margin-top: 20px; text-align: left; }
  .services { position: absolute; left: 731px; top: 408px; }
  .services h2 {
    color: var(--red); font-family: 'Montserrat', sans-serif; font-weight: 800; font-size: 20.5px; line-height: 27px;
  }
  .service-list { list-style: none; margin-top: 14px; font-family: 'Lato', sans-serif; font-size: 20.7px; line-height: 30.5px; color: var(--blue); }
  .service-list li { position: relative; padding-left: 29px; }
  .service-list li::before { content: "•"; position: absolute; left: 2px; }
  .address {
    position: absolute; left: 709px; width: 400px; top: 878px; text-align: center; color: var(--ink); font-style: normal;
    font-family: 'Montserrat', sans-serif; font-weight: 700; font-size: 17.5px; line-height: 25px;
  }
  .address .divider { margin: 0 16px; }
</style>
</head>
<body>
<main class="card">
  <svg class="backdrop" viewBox="0 0 2122 1736" preserveAspectRatio="none" aria-hidden="true">
    <polygon points="1087,1050 2122,565 2122,1736 1087,1736" fill="var(--mist)"/>
    <polygon points="480,0 1645,0 1087,262 1087,220 480,220" fill="var(--yellow)"/>
    <polygon points="0,0 480,0 480,220 1087,220 1087,650 555,650 0,390" fill="var(--red)"/>
    <rect x="0" y="946" width="1087" height="790" fill="var(--blue)"/>
    <polygon points="0,946 1087,946 1087,1060 0,1565" fill="var(--blue-deep)"/>
  </svg>

  <div class="portrait" role="img" aria-label="Portrait photo of Dr. Marisol Venhart"></div>

  <div class="languages">
    <div class="spanish">SE’ HABLA ESPANOL</div>
    <div class="tele">TELE-VISITS AVAILABLE</div>
  </div>

  <h1 class="doctor-name">MARISOL<br>VENHART, MD</h1>

  <div class="headline">
    <div class="cares">A DOCTOR WHO CARES</div>
    <div class="trust">EXPERIENCE YOU CAN TRUST</div>
  </div>

  <div class="bio">
    <p><strong>Dr. Venhart</strong> has been practicing medicine in Brookfield for over 12 years. She was previously a primary care doctor with St. Brigid Harlow Clinic in Brookfield for 10 years. Dr. Venhart became dissatisfied with the assembly line fashion of medical care and the pressure to spend minimal time with patients. Dr. Venhart choose to go out on her own to deliver medical care the way she believes it should be practiced. Dr. Venhart prides herself on delivering the individual care that patients require no matter the time required.</p>
    <p>Dr. Venhart maintains hospital privileges at Halden/St. Brigid, Marlow, Ashford.</p>
  </div>

  <section class="services">
    <h2>ALL PRIMARY CARE<br>SERVICES INCLUDING</h2>
    <ul class="service-list">
      <li>Hypertension (High Blood Pressure)</li>
      <li>Diabetes</li>
      <li>Colds</li>
      <li>Flu</li>
      <li>COVID</li>
      <li>Sports Physicals</li>
      <li>Auto Accidents/Slip &amp; Fall</li>
      <li>Blood Tests</li>
      <li>Back /Neck /Knee /Shoulder PAIN</li>
      <li>Vaccinations for Flu, Pneumonia</li>
      <li>Immigration examinations</li>
      <li>Social Security Examinations</li>
    </ul>
  </section>

  <address class="address">
    418 LINDEN AVENUE<br>
    BROOKFIELD, NJ 08190<span class="divider">|</span>555-014-7730
  </address>
</main>
</body>
</html>
```